We need a business card design for a new company located in Brampton Ontario Canada. Our goal is to promote companies to use our service as an "External Program Management " firm taking their industrial product concepts " from prototype to production." We would like to use blue and yellow as our colors. Our skills include finding suppliers for prototype parts and developing them into supplying not only prototypes but the final production parts as well for our customer base.
Industry/Entity Type
Business
Contact Information for Business Card
Dermot Kessing
Sales Manager
OLMERC Solutions Inc.
14 Fernhollow Lane
Brampton, Ontario L7P 2K9
Canada
Phone: 905-471-5928
Fax: 905-471-5928
website: www.olmercsolutions-example.com
Email: dermot@olmercsolutions-example.com

```html
<!DOCTYPE html>
<html lang="en">
<head>
<meta charset="utf-8">
<title>OLMERC Solutions Inc. – Business Card</title>
<link href="https://fonts.googleapis.com/css2?family=Exo+2:wght@400;500;700&display=swap" rel="stylesheet">
<style>
  :root {
    --page-bg: #e6e4e0;
    --brand-blue: #1b1be0;
    --brand-blue-deep: #0c0cb4;
    --brand-yellow: #f5c518;
    --card-white: #f7f7f7;
    --card-white-shade: #dedede;
    --text-light: #ffffff;
  }
  * { margin: 0; padding: 0; box-sizing: border-box; }
  html, body {
    width: 1200px; height: 900px; overflow: hidden;
    background: var(--page-bg);
    font-family: "Exo 2", sans-serif;
  }
  .business-card {
    position: absolute; left: 100px; top: 164px;
    width: 1000px; height: 572px;
    overflow: hidden;
    box-shadow: 0 10px 30px rgba(0,0,0,0.25);
  }
  .card-shapes { position: absolute; inset: 0; }
  .contact-side {
    position: absolute; left: 62px; top: 56px;
    color: var(--text-light);
  }
  .holder-name {
    font-size: 30px; font-weight: 500; letter-spacing: 2px;
    text-transform: uppercase;
  }
  .holder-title { font-size: 19px; margin-top: 2px; letter-spacing: 0.5px; }
  .office-address {
    font-size: 21px; line-height: 1.3; margin-top: 34px; font-style: normal;
  }
  .contact-list { list-style: none; margin-top: 30px; }
  .contact-item {
    display: flex; align-items: center; gap: 14px;
    font-size: 19px; letter-spacing: 1px; margin-bottom: 13px;
  }
  .contact-item.small { font-size: 14px; letter-spacing: 0.3px; }
  .contact-icon { width: 20px; height: 20px; flex: none; fill: var(--text-light); }
  .brand-mark {
    position: absolute; left: 566px; top: 210px;
    color: var(--brand-blue); font-weight: 700;
    line-height: 1;
  }
  .brand-name { font-size: 96px; letter-spacing: 2px; }
  .brand-suffix { font-size: 46px; margin-top: 6px; margin-left: 4px; }
</style>
</head>
<body>
  <section class="business-card">
    <svg class="card-shapes" width="1000" height="572" viewBox="0 0 1000 572">
      <defs>
        <linearGradient id="blueFill" x1="0" y1="0" x2="1" y2="1">
          <stop offset="0" stop-color="var(--brand-blue)"/>
          <stop offset="1" stop-color="var(--brand-blue-deep)"/>
        </linearGradient>
        <radialGradient id="whiteFill" cx="0.55" cy="0.45" r="0.7">
          <stop offset="0" stop-color="var(--card-white)"/>
          <stop offset="1" stop-color="var(--card-white-shade)"/>
        </radialGradient>
      </defs>
      <rect class="blue-field" width="1000" height="572" fill="url(#blueFill)"/>
      <path class="accent-crescent" d="M 600 20 C 370 140 340 420 470 560 L 500 572 C 370 420 400 140 640 0 Z" fill="var(--brand-yellow)"/>
      <path class="white-field" d="M 640 0 C 420 130 390 420 500 572 L 1000 572 L 1000 0 Z" fill="url(#whiteFill)"/>
    </svg>

    <div class="contact-side">
      <h1 class="holder-name">Dermot Kessing</h1>
      <p class="holder-title">Sales Manager</p>
      <address class="office-address">14 Fernhollow Lane<br>Brampton, Ontario L7P 2K9</address>
      <ul class="contact-list">
        <li class="contact-item">
          <svg class="contact-icon" viewBox="0 0 24 24"><path d="M6.6 10.8a15 15 0 0 0 6.6 6.6l2.2-2.2c.3-.3.7-.4 1-.2 1.1.4 2.3.6 3.6.6.6 0 1 .4 1 1V20c0 .6-.4 1-1 1A17 17 0 0 1 3 4c0-.6.4-1 1-1h3.5c.6 0 1 .4 1 1 0 1.3.2 2.5.6 3.6.1.3 0 .7-.2 1z"/></svg>
          <span>905-471-5928</span>
        </li>
        <li class="contact-item">
          <svg class="contact-icon" viewBox="0 0 24 24"><path d="M7 1h10a2 2 0 0 1 2 2v18a2 2 0 0 1-2 2H7a2 2 0 0 1-2-2V3a2 2 0 0 1 2-2zm0 3v14h10V4zm5 15.5a1 1 0 1 0 0 2 1 1 0 0 0 0-2z"/></svg>
          <span>905-471-5928</span>
        </li>
        <li class="contact-item">
          <svg class="contact-icon" viewBox="0 0 24 24"><path d="M6 2h9l3 3v5H6zm-2 9h16a2 2 0 0 1 2 2v7a2 2 0 0 1-2 2H4a2 2 0 0 1-2-2v-7a2 2 0 0 1 2-2zm3 3v2h2v-2zm4 0v2h2v-2zm4 0v2h2v-2z"/></svg>
          <span>905-471-5928</span>
        </li>
        <li class="contact-item small">
          <svg class="contact-icon" viewBox="0 0 24 24"><path d="M2 5h20v14H2zm2 2v.5l8 5.5 8-5.5V7zm0 3v7h16v-7l-8 5.5z"/></svg>
          <span>dermot@olmercsolutions-example.com</span>
        </li>
        <li class="contact-item small">
          <svg class="contact-icon" viewBox="0 0 24 24"><path d="M12 2a10 10 0 1 0 0 20 10 10 0 0 0 0-20zm6.9 6h-3a15 15 0 0 0-1.3-3.9A8 8 0 0 1 18.9 8zM12 4c.8 1.2 1.5 2.5 1.9 4h-3.8c.4-1.5 1.1-2.8 1.9-4zM4.3 14a8 8 0 0 1 0-4h3.4a16 16 0 0 0 0 4zm.8 2h3a15 15 0 0 0 1.3 3.9A8 8 0 0 1 5.1 16zm3-8h-3a8 8 0 0 1 4.3-3.9C8.8 5.3 8.4 6.6 8.1 8zM12 20c-.8-1.2-1.5-2.5-1.9-4h3.8c-.4 1.5-1.1 2.8-1.9 4zm2.3-6H9.7a14 14 0 0 1 0-4h4.6a14 14 0 0 1 0 4zm.3 5.9c.6-1.2 1-2.5 1.3-3.9h3a8 8 0 0 1-4.3 3.9zm1.7-5.9a16 16 0 0 0 0-4h3.4a8 8 0 0 1 0 4z"/></svg>
          <span>www.olmercsolutions-example.com</span>
        </li>
      </ul>
    </div>

    <div class="brand-mark">
      <div class="brand-name">OLMERC</div>
      <div class="brand-suffix">Solutions Inc.</div>
    </div>
  </section>
</body>
</html>
```